Pine Hollow Camp Brochure Design - TRI FOLD - See text examples added

Tri- Fold Brochure designed for Remote Alaskan Wilderness Fly-in lodge.We will provide several pictures. We want activities, directions, lodge rules, history, etc... We have provided our logo. Will work on adding text.
Looking for a professional, fun, adventurous feel.
Guests must fly in to the lodge. We are completely surrounded by wilderness. 33 miles from the nearest road. Take a 30 min flight seeing trip over mountains, glaciers, rivers and wildlife with Sky Tundrix to our private airstrip. Canoe in Heron Pond. See the Moose, Caribou, Bears, Lynx, wolves, and various birds. Go gold panning in the creeks.
Accommodations include your own private cabin with private bathroom. Access to the main lodge lounge and dining rooms, wood fired sauna, covered fire pit, and use of our canoe, life jackets, and rubber boots. Meals available. Wifi in main lodge. Movies in Theater.

Target Market(s)

Adventure, photographers, hikers, mountaineers, travelers

Industry/Entity Type

Tourism

Requirements
Must have
• Logo and pictures, information - Tri-Fold
Nice to have
• High quality attractive design with logo and information
Should not have
• Cartoony feel

```html
<!DOCTYPE html>
<html lang="en">
<head>
<meta charset="utf-8">
<title>Pine Hollow Camp – Tri-Fold Brochure</title>
<link rel="stylesheet" href="https://fonts.googleapis.com/css2?family=Fredoka:wght@500;600&family=Lato:wght@300;400;700&display=swap">
<style>
  :root{
    --paper:#ffffff;
    --canvas:#e9e9e6;
    --ink:#2a2d33;
    --body:#555a60;
    --accent:#e8501b;
    --fold:rgba(0,0,0,.10);
  }
  *{box-sizing:border-box;margin:0;padding:0}
  html,body{width:1200px;height:1200px;overflow:hidden;background:var(--canvas)}
  body{position:relative;font-family:'Lato',sans-serif;color:var(--body)}
  .spread{position:absolute;left:30px;width:1140px;display:flex;background:var(--paper);box-shadow:0 2px 8px rgba(0,0,0,.18)}
  .spread--outer{top:30px;height:540px}
  .spread--inner{top:600px;height:570px}
  .panel{position:relative;width:380px;height:100%}
  .panel + .panel{box-shadow:inset 6px 0 8px -6px var(--fold)}
  .panel__text{padding:36px 40px 0}
  .spread--outer .panel__text{height:270px}
  .spread--inner .panel__text{height:330px;padding-top:34px}
  h2{font-family:'Fredoka',sans-serif;font-weight:600;font-size:14px;letter-spacing:1.4px;text-transform:uppercase;color:var(--ink);margin-bottom:8px;line-height:1.25}
  h2.spaced{margin-top:18px}
  p{font-size:10.5px;font-weight:300;line-height:1.5;margin-bottom:9px}
  .hl{color:var(--accent);font-weight:700}
  .family-frame{position:absolute;left:100px;top:150px;width:160px;height:112px;background:#1f1f22;padding:8px;transform:rotate(5deg);box-shadow:2px 3px 6px rgba(0,0,0,.35)}
  .family-frame div{width:100%;height:100%;background:linear-gradient(160deg,#e7e3da,#c9c2b3)}
  .map{position:absolute;left:40px;top:160px;width:300px;height:100px;background:linear-gradient(90deg,#b9d69a 0%,#dfe3dc 22%,#ebebe8 70%,#dfe4ea 100%)}
  .map svg{position:absolute}
  .map span{position:absolute;font-family:'Fredoka',sans-serif;font-weight:600;font-size:11px;color:var(--accent);letter-spacing:1px}
  .cover{display:flex;flex-direction:column;align-items:center;justify-content:center;height:270px;gap:22px}
  .brand{display:flex;align-items:center;gap:12px;font-family:'Fredoka',sans-serif;font-weight:600;font-size:30px;color:var(--ink);letter-spacing:1px}
  .brand i{display:block;width:18px;height:18px;border-radius:50%;background:var(--accent)}
  .site{font-family:'Fredoka',sans-serif;font-weight:600;font-size:11.5px;letter-spacing:1.6px;color:var(--ink)}
  .landscape{position:absolute;left:0;top:270px;width:1140px;height:230px;background:linear-gradient(180deg,#8e9bb3 0%,#c9b7b8 26%,#6d5350 40%,#4b4a36 58%,#c5a7a3 70%,#3f3b2c 85%,#7e6740 100%)}
  .band-copy{position:absolute;top:270px;height:230px;width:380px;display:flex;flex-direction:column;align-items:center;justify-content:center;text-align:center;color:#fff;padding:0 44px}
  .band-copy p{font-size:10.5px;font-weight:400;margin:0 0 10px;line-height:1.45}
  .band-copy hr{width:100px;border:0;border-top:2px solid #fff;margin:12px 0}
  .photo{position:absolute;left:0;top:330px;width:100%;height:200px}
  .photo--lodge{background:linear-gradient(180deg,#6f8fc4 0%,#b7c3cf 38%,#3b3a30 62%,#5b6a3c 100%)}
  .photo--moose{background:radial-gradient(circle at 55% 55%,#5a3a24 0%,#3b2718 45%,#6d5a47 100%)}
  .photo--cabin{background:linear-gradient(90deg,#3f5a33 0%,#6b4a2e 30%,#e9e7e1 60%,#5a3d27 100%)}
</style>
</head>
<body>

<section class="spread spread--outer">
  <div class="panel">
    <div class="panel__text">
      <h2>Hosts</h2>
      <p>We are the Halvorsens, your hosts at the Pine Hollow Camp and a family of 12 who live in Alaska and love to share their experience with others. Spend your time with us hiking one of several marked trails, climbing Mt. Anderson, using our canoe on Heron Pond, gold panning the creeks, and much more!</p>
    </div>
    <div class="family-frame"><div role="img" aria-label="Framed drawing of the host family"></div></div>
  </div>
  <div class="panel">
    <div class="panel__text">
      <h2>Directions</h2>
      <p>This is a remote property completely surrounded by wilderness and 33 miles from the nearest road, so guests must fly in to the lodge. From Healy airport, Sky Tundrix will take you on a 30 min scenic tour of mountains, rivers, glaciers and wildlife. Upon arrival at Pine Hollow Camp, our staff will greet you and give you a tour of the property including over 25 historic buildings.</p>
    </div>
    <div class="map" role="img" aria-label="Map showing the route from Healy to the lodge">
      <svg width="14" height="18" viewBox="0 0 14 18" style="left:16px;top:20px"><path d="M7 0a7 7 0 0 1 7 7c0 5-7 11-7 11S0 12 0 7a7 7 0 0 1 7-7z" fill="#e8501b"/><circle cx="7" cy="7" r="2.6" fill="#fff"/></svg>
      <span style="left:36px;top:23px">HEALY</span>
      <svg width="14" height="18" viewBox="0 0 14 18" style="left:186px;top:56px"><path d="M7 0a7 7 0 0 1 7 7c0 5-7 11-7 11S0 12 0 7a7 7 0 0 1 7-7z" fill="#e8501b"/><circle cx="7" cy="7" r="2.6" fill="#fff"/></svg>
      <span style="left:136px;top:61px">LODGE</span>
    </div>
  </div>
  <div class="panel">
    <div class="cover">
      <div class="brand"><i></i>Pine Hollow Camp</div>
      <div class="site">WWW.PINEHOLLOWALASKA.COM</div>
    </div>
  </div>

  <div class="landscape" role="img" aria-label="Panorama of an Alaskan lake reflecting mountains at dusk with spruce trees"></div>
  <div class="band-copy" style="left:0">
    <hr><p>You sleep in your own cabin but it's here, in the main lodge, where friends are made and stories shared.</p><hr>
  </div>
  <div class="band-copy" style="left:380px">
    <p>Pine Hollow Camp can accommodate families, large groups, prolonged stays, and custom vacation types.</p>
    <p>Private cabins and private bathrooms!</p><hr>
  </div>
  <div class="band-copy" style="left:760px">
    <hr><p>Offering the same spectacular mountainous surroundings as Denali without the crowds.</p><hr>
  </div>
</section>

<section class="spread spread--inner">
  <div class="panel">
    <div class="panel__text">
      <h2>Welcome to Pine Hollow<br>Camp, Est. 1898!</h2>
      <p>Set among 1.2 million acres of splendid wilderness deep in the Alaska Range, this is the <span class="hl">REAL ALASKA!</span> Ideal for adventure travelers, wildlife enthusiasts, photographers, hikers, or just about anyone in search of the last best place on earth.</p>
      <p>Take a 30 min sightseeing flight from Healy airport to the heart of the mountainous Alaska Range, where PHC is nestled at the base of Mt. Anderson and directly on the Pine Creek.</p>
      <p>This is truly a wilderness lodge and we invite everyone to partake in the many outdoor activities or simply relax by the firepit, converse in the lounge, or watch the Dall sheep on Mt. Anderson from the dining room.</p>
    </div>
    <div class="photo photo--lodge" role="img" aria-label="Photo of the log main lodge beneath a snowy peak"></div>
  </div>
  <div class="panel">
    <div class="panel__text">
      <h2>Activities</h2>
      <p>Start your adventure with Sky Tundrix as they show you the mountains, rivers, glaciers, and wildlife from the air. Once you land at Pine Hollow Camp, our friendly staff will give you a tour of the rustic buildings and trailheads, the main lodge lounge and dining areas, and show you to your private cabins.</p>
      <p>As well as their cabin and the main lodge, guests have access to the Aurora <span class="hl">Theater</span>, wood fired <span class="hl">sauna</span>, covered <span class="hl">fire pit</span>, <span class="hl">trapper's cabin</span> museum, lodge grounds, and all of the surrounding public land including 10 <span class="hl">hiking</span> trails and 2 <span class="hl">lakes</span>. We have <span class="hl">canoes</span>, life jackets, and rubber boots available to use at the lakes, or even to go <span class="hl">gold panning</span> in the creeks! You can go <span class="hl">wildlife watching</span> just about anywhere for moose, caribou, bears, lynx, wolves, and various birds.</p>
    </div>
    <div class="photo photo--moose" role="img" aria-label="Close-up photo of a bull moose with antlers"></div>
  </div>
  <div class="panel">
    <div class="panel__text">
      <h2>The Lodge</h2>
      <p>Our two-story lodge is made of hand-hewn spruce and 15 years of short summers, with each log individually dragged to the site by horse and dog sled. The inviting lodge features a lounge where guests relax on sofas with a glass of wine or a cocktail before dinner.</p>
      <h2 class="spaced">Accommodation</h2>
      <p>Stay in one of our private cabins with private bathroom, hot water, baseboard heat or wood stove for <span class="hl">$139/night</span> per cabin. Cabins can have a single queen, a queen and single, or two singles and a queen. Breakfast included, and wifi available in main lodge.</p>
    </div>
    <div class="photo photo--cabin" role="img" aria-label="Photo of a small log guest cabin among spruce trees"></div>
  </div>
</section>

</body>
</html>
```